New Brand - Website Design (4 Pages)

We are launching a new brand for electronic cigarettes. We already have logo and packaging done and would like a web design to go with it.

We are interested in the following deliverables:

1) Home Page Design
2) Check Out Design
3) How it Works Page
4) Secondary Template Page Design

Looking for a 60s modern look and something that is consistent with our logo and packaging.

Industry/Entity Type

Electronic

Requirements
Must have
• Consistent with logo and packaging (Use Logo Attached)
White background

Example (Functionality & Design): http://www.torvex.co.uk/
Example (Design): http://www.quillharbor.com/

We want the design more like quillharbor but the functionality the same as torvex.

Top Bar: Pebble Arcs Kits; Cartridge Refills; How it Works; Contact; My Account; Checkout
Should not have
• Stock List or Search Bar or Newsletter Signup

```html
<!DOCTYPE html>
<html lang="en">
<head>
<meta charset="utf-8">
<title>Checkout — Pebble Arcs</title>
<link rel="stylesheet" href="https://fonts.googleapis.com/css2?family=Josefin+Sans:wght@300;400;600&family=Open+Sans:wght@400;600;700&family=Oswald:wght@200;300;400&display=swap">
<style>
:root{
  --ink:#000;
  --paper:#fff;
  --sky:#8fd8f6;
  --sky-soft:#b6e4f8;
  --panel:#f1f2f3;
  --line:#dcdfe2;
  --field:#e3e5e7;
  --text:#333;
  --muted:#777;
  --req:#b0161c;
  --link:#8a7a2a;
  --notice:#f1f8fc;
  --notice-line:#bfe3f2;
  --box-red:#c9472c;
}
*{box-sizing:border-box;margin:0;padding:0}
html,body{width:1200px;height:1190px;overflow:hidden;background:var(--paper)}
body{position:relative;font-family:"Open Sans",Arial,sans-serif;color:var(--text);font-size:14px}
.abs{position:absolute}

.site-header{position:absolute;left:0;top:0;width:1200px;height:153px;background:var(--ink)}
.main-nav{position:absolute;left:0;top:0;width:800px;height:153px;font-family:"Oswald",sans-serif;font-weight:200;font-size:20px;line-height:26px;color:var(--paper)}
.main-nav span{position:absolute;top:108px;white-space:nowrap}
.main-nav .current{font-weight:400}
.brand{position:absolute;left:810px;top:22px;display:flex;align-items:center}
.brand-dot{width:116px;height:108px;border-radius:50%;background:var(--sky)}
.brand-name{margin-left:22px;font-family:"Josefin Sans",sans-serif;font-weight:400;font-size:46px;line-height:1;color:var(--paper);letter-spacing:3px}

.coupon{left:105px;top:170px;width:935px;height:67px;background:var(--notice);border:1px solid var(--notice-line);border-radius:3px;box-shadow:0 1px 2px rgba(0,0,0,.08);padding:23px 19px;font-size:14px}
.coupon a{color:var(--link);text-decoration:none}

.section-title{font-size:22px;font-weight:700;color:#444}
.label{font-size:14px;color:#444}
.label b{color:var(--req);font-weight:400}
.field{position:absolute;height:30px;border:1px solid var(--field);background:var(--paper);font-size:13px;color:#aaa;padding:6px 7px}
.select{position:absolute;height:30px;border:1px solid #aaa;border-radius:3px;background:linear-gradient(#fff,#eee);font-size:12px;color:#444;padding:6px 8px}
.select::after{content:"";position:absolute;right:10px;top:11px;border:4px solid transparent;border-top:5px solid #666}
.note{font-size:14px;line-height:25px;color:#444}

.order-table{left:592px;top:303px;width:448px;height:205px;border:1px solid var(--line)}
.order-head{position:absolute;left:0;top:0;width:448px;height:40px;background:var(--sky);font-family:"Josefin Sans",sans-serif;font-weight:600;font-size:26px;color:#000}
.product-shot{left:627px;top:350px;width:67px;height:66px;background:linear-gradient(135deg,#2a2a2a 0 60%,var(--box-red) 60%)}
.row-label{position:absolute;background:var(--sky-soft);font-family:"Josefin Sans",sans-serif;font-size:13px;color:#000;text-align:right;padding-right:24px}
.money{position:absolute;font-size:13px;color:#444}

.payment{left:592px;top:556px;width:448px;height:436px;border:1px solid var(--line)}
.card-fields{position:absolute;left:0;top:60px;width:448px;height:204px;background:var(--panel);border-top:1px solid var(--line);border-bottom:1px solid var(--line)}
.small{font-size:11.5px;color:#555}
.mini-select{position:absolute;height:17px;border:1px solid #999;border-radius:3px;background:linear-gradient(#fff,#eee);font-size:10.5px;color:#000;padding:1px 6px}
.check{display:inline-flex;align-items:center;margin-right:15px;font-size:14px;color:#555}
.check svg{margin-right:7px}
.place-order{left:608px;top:933px;width:419px;height:46px;background:var(--sky);font-family:"Josefin Sans",sans-serif;font-weight:600;font-size:24px;color:#000;text-align:center;line-height:50px}

.site-footer{position:absolute;left:0;top:1142px;width:1200px;height:48px;background:var(--ink);font-family:"Oswald",sans-serif;font-weight:200;font-size:13px;color:var(--paper);text-align:right;padding:15px 18px 0 0}
</style>
</head>
<body>

<header class="site-header">
  <nav class="main-nav">
    <span style="left:18px">HOME</span>
    <span style="left:90px">PEBBLE ARCS KITS</span>
    <span style="left:234px">CARTRIDGE REFILLS</span>
    <span style="left:414px">HOW IT WORKS</span>
    <span style="left:558px">MY ACCOUNT</span>
    <span class="current" style="left:703px">CHECKOUT</span>
  </nav>
  <div class="brand">
    <div class="brand-dot"></div>
    <div class="brand-name">PEBBLE<br>ARCS</div>
  </div>
</header>

<div class="abs coupon">Have a coupon? <a href="#">Click here to enter your code</a></div>

<h2 class="abs section-title" style="left:105px;top:265px">Billing Address</h2>

<div class="abs label" style="left:105px;top:314px">Country <b>*</b></div>
<div class="select" style="left:105px;top:337px;width:448px">South Africa</div>

<div class="abs label" style="left:105px;top:395px">First Name <b>*</b></div>
<div class="field" style="left:105px;top:418px;width:214px"></div>
<div class="abs label" style="left:339px;top:395px">Last Name <b>*</b></div>
<div class="field" style="left:339px;top:418px;width:214px"></div>

<div class="abs label" style="left:105px;top:477px">Company Name</div>
<div class="field" style="left:105px;top:498px;width:448px"></div>

<div class="abs label" style="left:105px;top:557px">Address <b>*</b></div>
<div class="field" style="left:105px;top:580px;width:448px">Street address</div>
<div class="field" style="left:105px;top:630px;width:448px">Apartment, suite, unit etc. (optional)</div>

<div class="abs label" style="left:105px;top:689px">Town / City <b>*</b></div>
<div class="field" style="left:105px;top:712px;width:448px">Town / City</div>

<div class="abs label" style="left:105px;top:771px">Province <b>*</b></div>
<div class="select" style="left:105px;top:794px;width:214px">Select an option…</div>
<div class="abs label" style="left:339px;top:771px">Postcode / Zip <b>*</b></div>
<div class="field" style="left:339px;top:794px;width:214px">Postcode / Zip</div>

<div class="abs label" style="left:105px;top:853px">Email Address <b>*</b></div>
<div class="field" style="left:105px;top:876px;width:214px"></div>

<p class="abs note" style="left:105px;top:926px;width:450px">Create an account by entering the information below. If you are a returning customer please login at the top of the page.</p>

<div class="abs label" style="left:105px;top:989px">Account username</div>
<div class="field" style="left:105px;top:1010px;width:214px">Username</div>

<div class="abs label" style="left:105px;top:1069px">Account password</div>
<div class="field" style="left:105px;top:1090px;width:214px">Password</div>
<div class="abs label" style="left:339px;top:1069px">Confirm password</div>
<div class="field" style="left:339px;top:1090px;width:214px">Confirm password</div>

<h2 class="abs section-title" style="left:593px;top:265px">Your order</h2>

<div class="abs order-table">
  <div class="order-head"><span class="abs" style="left:7px;top:9px">PRODUCT</span><span class="abs" style="left:339px;top:9px">TOTAL</span></div>
  <div class="abs" style="left:317px;top:40px;width:1px;height:165px;background:var(--line)"></div>
  <div class="row-label" style="left:0;top:121px;width:318px;height:38px;border-top:3px solid var(--sky);padding-top:18px">SUB TOTAL</div>
  <div class="row-label" style="left:0;top:162px;width:318px;height:40px;border-top:3px solid var(--sky);border-bottom:3px solid var(--sky);padding-top:13px">TOTAL</div>
  <div class="abs" style="left:318px;top:121px;width:130px;height:1px;background:var(--line)"></div>
  <div class="abs" style="left:318px;top:162px;width:130px;height:1px;background:var(--line)"></div>
  <span class="money" style="left:370px;top:72px">$99</span>
  <span class="money" style="left:370px;top:134px">$99</span>
  <span class="money" style="left:370px;top:175px;font-weight:700;color:#000">$99</span>
</div>
<div class="abs product-shot" role="img" aria-label="Product box of the Pebble Arcs starter kit"></div>
<div class="abs" style="left:722px;top:356px;font-family:'Josefin Sans',sans-serif;font-weight:300;font-size:19px;line-height:22px;color:#000">Product Description<br>Qty: 1</div>

<div class="abs payment">
  <svg class="abs" style="left:15px;top:24px" width="14" height="14" viewBox="0 0 14 14"><circle cx="7" cy="7" r="6" fill="#fff" stroke="#999"/><circle cx="7" cy="7" r="3" fill="#3a7bd5"/></svg>
  <span class="abs" style="left:41px;top:21px;font-size:15px;color:#555">Credit Card</span>
  <div class="abs" style="left:359px;top:18px;width:30px;height:22px;background:#e9eef6;border:1px solid #b8c4d6;border-radius:2px"></div>
  <div class="abs" style="left:392px;top:18px;width:31px;height:22px;background:#2e4f8f;border-radius:2px"></div>
  <div class="card-fields">
    <div class="abs" style="left:14px;top:10px;width:326px;height:33px;background:#fff;font-family:'Josefin Sans',sans-serif;font-size:12px;line-height:15px;color:#000;padding:5px 0 0 1px">NOTE: A MERCHANT ACCOUNT IS REQUIRED<br>FOR CREDIT CARD PAYMENT - NOT INCLUDED</div>
    <span class="abs small" style="left:16px;top:54px">Credit Card number <b style="color:var(--req);font-weight:400">*</b></span>
    <div class="abs" style="left:16px;top:72px;width:199px;height:30px;background:#fff;border:1px solid var(--field)"></div>
    <span class="abs small" style="left:232px;top:54px">Card type <b style="color:var(--req);font-weight:400">*</b></span>
    <div class="mini-select" style="left:232px;top:72px;width:199px">Paycrest</div>
    <span class="abs small" style="left:16px;top:117px">Expiration date <b style="color:var(--req);font-weight:400">*</b></span>
    <div class="mini-select" style="left:16px;top:137px;width:94px">Month</div>
    <div class="mini-select" style="left:114px;top:137px;width:94px">Year</div>
    <span class="abs small" style="left:232px;top:117px">Card security code <b style="color:var(--req);font-weight:400">*</b></span>
    <div class="abs" style="left:232px;top:135px;width:43px;height:30px;background:#fff;border:1px solid var(--field)"></div>
    <span class="abs small" style="left:282px;top:135px;line-height:20px">3 or 4 digits usually found<br>on the signature strip.</span>
  </div>
  <div class="abs" style="left:16px;top:280px;font-size:16px;font-weight:600;color:#444">Want to keep updated about our products?</div>
  <div class="abs" style="left:16px;top:318px;display:flex">
    <span class="check"><svg width="13" height="13" viewBox="0 0 13 13"><rect x=".5" y=".5" width="12" height="12" fill="#fff" stroke="#888"/><path d="M3 6.5l2.5 3L11 2" fill="none" stroke="#2b4f8a" stroke-width="2"/></svg>General News</span>
    <span class="check"><svg width="13" height="13" viewBox="0 0 13 13"><rect x=".5" y=".5" width="12" height="12" fill="#fff" stroke="#888"/><path d="M3 6.5l2.5 3L11 2" fill="none" stroke="#2b4f8a" stroke-width="2"/></svg>The One Pager</span>
    <span class="check"><svg width="13" height="13" viewBox="0 0 13 13"><rect x=".5" y=".5" width="12" height="12" fill="#fff" stroke="#888"/><path d="M3 6.5l2.5 3L11 2" fill="none" stroke="#2b4f8a" stroke-width="2"/></svg>Cartwell</span>
  </div>
  <div class="abs" style="left:16px;top:346px;font-size:13px;font-style:italic;color:#888">You can always change your list subscription settings <a href="#" style="color:#2a6db5;text-decoration:none">here</a>.</div>
</div>
<div class="abs place-order">PLACE ORDER</div>

<footer class="site-footer">COPYRIGHT 2013 PEBBLE ARCS</footer>

</body>
</html>
```